Energy Healing for pregnant women postcard

I am an intuitive energy healer specializing in the care of pregnant women and their babies. I have an existing logo that is attached that should be placed on the card,sizing is at your discretion, recolor as needed. The message of the card should be one that conveys tranquility, growth, life and light. Images of pregnancy and motherhood could also fit well on the card, but that is not required if the preceding messages can be conveyed through other imagery. Also on the card, the following should appear: (company name and tag line)Positivity & JoyHealing the mind, body, spirit and soul with Energy provided to all living things by the Universe. Space should be left for my name and credentials on the front, while the address space on the back will be used for more contact information. Opposite the address block on the back, please leave room for a text box that will include benefits of the services. About 2"x3" should suffice.

Target Market(s)

Pregnant women and newly post-partum women

Industry/Entity Type

Health And Wellness

Font styles to use
Script

Colors
b05ba4
b768aa
d3a5cc
ecdaeb
e7f5f8
cfdeed
cee9f5
85cae6

Requirements
Must have
• Company logo. Company name. Tag line. Individual name and certifications
Nice to have
• Pictures or images that convey peace, tranquility healing and growth.
Should not have
• Anything harsh.

```html
<!DOCTYPE html>
<html lang="en">
<head>
<meta charset="utf-8">
<title>Harbor &amp; Fern – Energy Healing Postcard</title>
<link rel="stylesheet" href="https://fonts.googleapis.com/css2?family=Cormorant+Garamond:ital,wght@1,600;1,700&family=Archivo+Narrow:wght@600;700&display=swap">
<style>
  :root {
    --page: #ffffff;
    --purple-deep: #6a1aa8;
    --purple-mid: #9a3fd0;
    --purple-light: #c070e0;
    --glow-white: #fdf6ff;
    --lotus-pink: #e6b8f0;
    --aqua: #8fe4ea;
    --aqua-soft: #cee9f5;
    --text-white: #ffffff;
    --card-edge: #d8d8d8;
  }
  * { box-sizing: border-box; margin: 0; padding: 0; }
  html, body {
    width: 801px; height: 1200px; overflow: hidden;
    background: var(--page);
  }
  .canvas { position: relative; width: 801px; height: 1200px; }

  /* ---------- Front of card ---------- */
  .card-front {
    position: absolute; left: 31px; top: 30px; width: 712px; height: 546px;
    overflow: hidden;
    background: linear-gradient(100deg, var(--purple-deep) 0%, var(--purple-mid) 45%, var(--purple-light) 100%);
  }
  .front-art {
    position: absolute; right: 0; top: 0; width: 340px; height: 546px;
    background:
      radial-gradient(ellipse 60% 30% at 70% 78%, var(--glow-white) 0%, rgba(253,246,255,0.75) 45%, rgba(230,184,240,0) 100%),
      radial-gradient(ellipse 55% 60% at 75% 30%, rgba(255,240,255,0.55) 0%, rgba(230,184,240,0) 80%);
  }
  .tagline {
    position: absolute; left: 47px; top: 50px; width: 640px;
    font-family: "Cormorant Garamond", serif; font-style: italic; font-weight: 700;
    font-size: 28px; line-height: 37px; color: var(--aqua);
    text-shadow: 0 0 4px rgba(40,0,80,0.6);
  }
  .brand {
    position: absolute; left: 85px; top: 236px; width: 240px;
    display: flex; align-items: center; justify-content: center; gap: 8px;
    font-family: "Archivo Narrow", sans-serif; font-weight: 700;
    font-size: 30px; color: var(--aqua);
  }
  .brand-dot {
    width: 12px; height: 12px; border-radius: 50%; background: var(--aqua);
  }
  .front-credentials {
    position: absolute; left: 37px; top: 386px; width: 340px; text-align: center;
    font-family: "Archivo Narrow", sans-serif; font-weight: 700;
    color: var(--aqua); text-shadow: 0 0 3px rgba(40,0,80,0.5);
  }
  .front-credentials .name { font-size: 23px; font-variant: small-caps; line-height: 28px; }
  .front-credentials .line { font-size: 17px; line-height: 23px; }

  /* ---------- Back of card ---------- */
  .card-back {
    position: absolute; left: 34px; top: 600px; width: 709px; height: 544px;
    background: var(--page); border: 1px solid var(--card-edge);
  }
  .benefits-panel {
    position: absolute; left: 0; top: 0; width: 370px; height: 511px; overflow: hidden;
    background: linear-gradient(260deg, var(--purple-deep) 0%, var(--purple-mid) 50%, var(--purple-light) 100%);
    color: var(--text-white);
    font-family: "Archivo Narrow", sans-serif; font-weight: 600;
  }
  .back-art {
    position: absolute; left: 0; top: 60px; width: 150px; height: 451px;
    background:
      radial-gradient(ellipse 70% 30% at 10% 80%, var(--glow-white) 0%, rgba(253,246,255,0.6) 45%, rgba(230,184,240,0) 100%),
      radial-gradient(ellipse 60% 45% at 20% 30%, rgba(255,240,255,0.45) 0%, rgba(230,184,240,0) 80%);
  }
  .back-head {
    position: absolute; left: 0; top: 28px; width: 370px; text-align: center;
  }
  .back-head .name { font-size: 18px; font-weight: 700; font-variant: small-caps; line-height: 22px; }
  .back-head .line { font-size: 14px; line-height: 20px; }
  .contact {
    position: absolute; left: 0; top: 108px; width: 370px; text-align: center;
    font-size: 19px; font-weight: 700; line-height: 25px;
  }
  .divider {
    position: absolute; left: 140px; top: 182px; width: 108px; height: 3px;
    background: var(--text-white); border-radius: 2px;
  }
  .benefits {
    position: absolute; left: 137px; top: 226px; width: 230px; list-style: none;
    font-size: 15px; line-height: 21px;
  }
  .benefits li { position: relative; padding-left: 24px; margin-bottom: 4px; }
  .benefits svg { position: absolute; left: 0; top: 4px; width: 12px; height: 12px; }
</style>
</head>
<body>
<main class="canvas">

  <section class="card-front" aria-label="Postcard front">
    <div class="front-art" role="img" aria-label="White lotus flower on still water with a shower of sparkling light"></div>
    <p class="tagline">Healing the mind, body, spirit and soul with Energy provided to all living things by the Universe.</p>
    <div class="brand"><span class="brand-dot"></span>Harbor &amp; Fern</div>
    <div class="front-credentials">
      <p class="name">Marisol K. Brandt</p>
      <p class="line">MSN, RCMT</p>
      <p class="line">Reiki Master Teacher,</p>
      <p class="line">Archangelic Light Master Teacher</p>
    </div>
  </section>

  <section class="card-back" aria-label="Postcard back">
    <div class="benefits-panel">
      <div class="back-art" role="img" aria-label="White lotus petals and sparkling light"></div>
      <div class="back-head">
        <p class="name">Marisol K. Brandt, msn, rcmt</p>
        <p class="line">Reiki Master Teacher,</p>
        <p class="line">Archangelic Light Master Teacher</p>
      </div>
      <div class="contact">
        <p>555.240.8816</p>
        <p>hello@harborfern.com</p>
      </div>
      <div class="divider" role="img" aria-label="Decorative divider"></div>
      <ul class="benefits">
        <li><svg viewBox="0 0 12 12"><path d="M6 0 L7 5 L12 6 L7 7 L6 12 L5 7 L0 6 L5 5 Z" fill="#fff"/></svg>Deep relaxation</li>
        <li><svg viewBox="0 0 12 12"><path d="M6 0 L7 5 L12 6 L7 7 L6 12 L5 7 L0 6 L5 5 Z" fill="#fff"/></svg>Decrease anxiety</li>
        <li><svg viewBox="0 0 12 12"><path d="M6 0 L7 5 L12 6 L7 7 L6 12 L5 7 L0 6 L5 5 Z" fill="#fff"/></svg>Decrease stress</li>
        <li><svg viewBox="0 0 12 12"><path d="M6 0 L7 5 L12 6 L7 7 L6 12 L5 7 L0 6 L5 5 Z" fill="#fff"/></svg>Decrease discomforts</li>
        <li><svg viewBox="0 0 12 12"><path d="M6 0 L7 5 L12 6 L7 7 L6 12 L5 7 L0 6 L5 5 Z" fill="#fff"/></svg>Promote feelings of wellbeing</li>
        <li><svg viewBox="0 0 12 12"><path d="M6 0 L7 5 L12 6 L7 7 L6 12 L5 7 L0 6 L5 5 Z" fill="#fff"/></svg>Promote balance</li>
        <li><svg viewBox="0 0 12 12"><path d="M6 0 L7 5 L12 6 L7 7 L6 12 L5 7 L0 6 L5 5 Z" fill="#fff"/></svg>Relieve physical discomforts of pregnancy</li>
      </ul>
    </div>
  </section>

</main>
</body>
</html>
```